依頼詳細
PCとスマホデザインの両方納品をいただきますが、
まずはデザインイメージが確認しやすいPCページのみの提案をお願いします。
スマホページは当選者に納品時にお願いしたいと思います。
スマホサイズについて、カンバスサイズは横幅375pxで作成し、2倍の横幅750pxのサイズで書き出ししてください。
(Retinaディスプレイに対応するため)
スマホページ作成時は、メニューが展開した際のデザインもお願いします。
レスポンシブウェブデザインを意識したデザインでお願いします。

■サイトマップ
添付の画面遷移図をご確認ください。

■参考サイト
https://harbor-mend-crew.com/
https://www.qv-tm.co.jp/

■内容について
工場や倉庫の修繕・改修・増築などを専門とするサービスサイトになります。

■素材写真
画像データについては、フリー素材から流用して
イメージ画像に当て込んでください。
足りない場合は、一旦他のサイトの写真をサンプルとして
入れてください。(サンプルなどの表記をお願いします)
また、購入が必要な写真などを利用した場合、
価格とサイト名を教えてください。

また、Nimbrel Stockで定期契約をしていますので、
Nimbrel Stockの画像は使用できます。
デザイン時はカンプ画像をお入れいただきますようお願いします。

■ロゴについて
添付のロゴデータを使用してください。

■ワイヤーフレーム
https://mk.velquora.com/view/600e5e1a-e3bd-4b32-a74b-244a4501d661-355d/?fullscreen
コンテンツの構成としてワイヤーフレームを作成しましたが
必ずしもワイヤーフレームの通りではなくて大丈夫です。
TOPページに配置するコンテンツを見ていただき、デザインは
デザイナーの皆様におまかせしたいと思います。

----------------------------------------------------------------------------
【制作物に対するお願い】

■フォントについて
・無料で使えるフォントで作成をお願いします。
・OSに紐づくフォントの使用は控えていただければと思います (ヒラギノなど)

サイトURL
ページ数
1ページ
希望イメージ
シンプル 複雑
単色 カラフル
暗い 明るい
日常 高級
遊び心 厳粛
未来的 伝統的
女性的 男性的
希望する色
ベースカラー:白、ポイントカラー:赤、青(救急のイメージ)
納品ファイル
• 高解像度JPG (.jpg)
• イラストレーター形式 (.ai)
• フォトショップ形式 (.psd)
補足説明
上記のいずれか1つ(アウトラインありとなしの2つ)と高解像度JPGを納品お願いします。
adobe XDでの納品も可能です。

```html
<!DOCTYPE html>
<html lang="ja">
<head>
<meta charset="UTF-8">
<title>工場修繕センター | 工場・倉庫の修繕・改修・増築</title>
<link href="https://fonts.googleapis.com/css2?family=Noto+Sans+JP:wght@400;500;700;900&family=Montserrat:ital,wght@1,600;1,700&display=swap" rel="stylesheet">
<style>
:root{
  --red:#e0262b;
  --blue:#1e78d2;
  --blue-dark:#17529c;
  --navy:#163f78;
  --sky:#e7f2fc;
  --ink:#222b36;
  --muted:#6a7480;
  --line:#d7e1eb;
  --white:#fff;
}
*{box-sizing:border-box;margin:0;padding:0}
html,body{width:1200px;height:4612px;overflow:hidden}
body{font-family:"Noto Sans JP",sans-serif;color:var(--ink);background:var(--white);position:relative}
.img{position:absolute;border-radius:6px}
.en{font-family:"Montserrat",sans-serif;font-style:italic;font-weight:600;letter-spacing:.08em;font-size:16px}

/* header */
.site-header{position:absolute;top:0;left:0;width:1200px;height:128px;background:var(--white)}
.logo{position:absolute;left:22px;top:30px;display:flex;align-items:center;gap:8px}
.logo-mark{width:26px;height:26px;background:var(--red);border-radius:4px}
.logo-name{font-weight:900;font-size:22px;color:var(--blue-dark)}
.header-lead{position:absolute;left:260px;top:18px;width:290px;font-size:10px;line-height:1.5;color:var(--muted)}
.header-tel{position:absolute;left:580px;top:14px;font-size:30px;font-weight:900;color:var(--blue-dark);display:flex;align-items:center;gap:8px}
.header-btns{position:absolute;right:0;top:0;display:flex}
.header-btns a{width:160px;height:60px;color:#fff;font-size:13px;font-weight:700;text-decoration:none;display:flex;align-items:center;justify-content:center}
.btn-mail{background:var(--blue)}
.btn-line{background:#7ac143}
.gnav{position:absolute;left:190px;top:80px;display:flex}
.gnav a{font-size:13px;font-weight:700;color:var(--ink);text-decoration:none;padding:0 18px;border-left:1px solid var(--line)}
.gnav a:first-child{border-left:none}

/* hero */
.hero{position:absolute;top:128px;left:0;width:1200px;height:600px;overflow:hidden}
.hero-bg{position:absolute;inset:0;background:linear-gradient(180deg,#7fb6e8 0%,#cfe3f5 45%,#9fb2c6 100%)}
.hero-copy{position:absolute;left:240px;top:90px;width:820px;text-align:center}
.hero-catch{display:inline-block;background:var(--red);color:#fff;font-weight:900;font-size:40px;padding:4px 40px;transform:skewX(-8deg)}
.hero-sub{margin-top:18px;display:inline-block;background:var(--blue-dark);color:#fff;font-weight:700;font-size:22px;padding:6px 24px}
.hero-main{margin-top:18px;display:inline-block;background:var(--blue);color:#fff;font-weight:900;font-size:66px;padding:4px 30px;letter-spacing:.04em}
.hero-line{margin-top:14px;display:inline-block;background:var(--blue-dark);color:#fff;font-weight:900;font-size:34px;padding:4px 26px}

/* section heading */
.sec-head{position:absolute;display:flex;flex-direction:column}
.sec-head .en{color:var(--muted)}
.sec-head h2{font-weight:900;font-size:44px;color:var(--red);line-height:1.2;display:flex;align-items:center;gap:12px}
.sec-head.light .en,.sec-head.light h2{color:#fff}
.icon-box{width:44px;height:44px;background:var(--red);border-radius:6px;display:flex;align-items:center;justify-content:center}
.pill{position:absolute;height:50px;border-radius:25px;background:var(--blue);color:#fff;font-size:15px;font-weight:700;display:flex;align-items:center;justify-content:center;gap:10px;text-decoration:none;box-shadow:0 4px 10px rgba(20,60,120,.25)}
.pill.white{background:#fff;color:var(--blue-dark)}

/* feature */
.feature-text{position:absolute;left:280px;top:930px;width:640px;font-size:14px;line-height:2;color:var(--ink)}
.feature-text p{margin-bottom:24px}

/* works */
.works-band{position:absolute;top:1440px;left:0;width:1200px;height:460px;background:var(--blue)}
.work-card{position:absolute;top:1600px;width:300px;height:280px;background:#fff;border-radius:8px;overflow:hidden;box-shadow:0 6px 16px rgba(0,0,0,.15)}
.work-card .ph{height:180px}
.work-card .meta{padding:14px 18px;font-size:13px;line-height:1.6}
.work-card .meta strong{display:block;color:var(--blue-dark);font-size:15px}
.arrow-dot{position:absolute;right:16px;bottom:22px;width:28px;height:28px;border-radius:50%;background:var(--blue);display:flex;align-items:center;justify-content:center}

/* column */
.col-card{position:absolute;background:#fff;border-radius:8px;box-shadow:0 6px 18px rgba(20,60,120,.15);overflow:hidden}
.col-date{font-size:11px;color:var(--muted)}
.col-title{font-size:16px;font-weight:700;color:var(--blue-dark);line-height:1.6}
.col-ex{font-size:12px;line-height:1.8;color:var(--ink)}

/* news */
.news-list{position:absolute;left:520px;top:2900px;width:560px}
.news-item{border-bottom:1px solid var(--line);padding:14px 0 20px}
.news-item time{font-size:11px;color:var(--muted);display:block;margin-bottom:6px}
.news-item p{font-size:14px;color:var(--blue-dark);line-height:1.8}

/* contents */
.contents-band{position:absolute;top:3340px;left:0;width:1200px;height:620px;background:linear-gradient(180deg,#d7e9f8,#eef6fd)}
.contents-box{position:absolute;top:3440px;left:130px;width:970px;height:440px;background:#fff;border-radius:10px;box-shadow:0 6px 20px rgba(20,60,120,.12)}
.menu-item{position:absolute;left:170px;width:370px;height:56px;border-bottom:1px solid var(--line);display:flex;align-items:center;gap:16px;font-size:17px;font-weight:700;color:var(--blue-dark)}
.menu-item .ic{width:40px;height:40px;border-radius:6px;background:var(--red);display:flex;align-items:center;justify-content:center}
.menu-item .chev{margin-left:auto}

/* contact */
.contact-lead{position:absolute;left:300px;top:4130px;font-size:14px;line-height:1.8}
.tel-box{position:absolute;left:700px;top:4000px;width:300px;height:96px;border:2px solid var(--blue);border-radius:8px;text-align:center;padding-top:8px}
.tel-box small{display:block;font-size:11px;color:var(--muted)}
.tel-box .num{font-size:30px;font-weight:900;color:var(--blue-dark);display:flex;align-items:center;justify-content:center;gap:8px}

/* footer */
.site-footer{position:absolute;top:4420px;left:0;width:1200px;height:192px;background:var(--navy);color:#fff}
.foot-logo{position:absolute;left:100px;top:36px;font-size:26px;font-weight:900}
.foot-tel{position:absolute;left:100px;top:84px;font-size:22px;font-weight:700;display:flex;gap:8px;align-items:center}
.foot-col{position:absolute;top:30px;font-size:11px;line-height:2.1}
.foot-copy{position:absolute;left:0;bottom:8px;width:1200px;display:flex;justify-content:space-between;padding:0 100px;font-size:10px;opacity:.8}
</style>
</head>
<body>

<header class="site-header">
  <div class="logo"><span class="logo-mark"></span><span class="logo-name">工場修繕センター</span></div>
  <p class="header-lead">新潟県内の工場・倉庫の修繕、改修、増築、外構工事、解体工事まで。プロの職人が迅速にお応えします。</p>
  <div class="header-tel">
    <svg width="26" height="26" viewBox="0 0 24 24"><path fill="#17529c" d="M6.6 10.8a15 15 0 0 0 6.6 6.6l2.2-2.2c.3-.3.7-.4 1-.2 1.1.4 2.3.6 3.6.6.6 0 1 .4 1 1V20c0 .6-.4 1-1 1A17 17 0 0 1 3 4c0-.6.4-1 1-1h3.5c.6 0 1 .4 1 1 0 1.3.2 2.5.6 3.6.1.3 0 .7-.2 1z"/></svg>
    0120-48-7315
  </div>
  <div class="header-btns"><a class="btn-mail" href="#">無料お見積り</a><a class="btn-line" href="#">お問い合わせ</a></div>
  <nav class="gnav">
    <a href="#">ホーム</a><a href="#">工場修繕センターの特徴</a><a href="#">サービス一覧</a><a href="#">施工実績</a><a href="#">会社概要</a><a href="#">よくあるご質問</a><a href="#">お問い合わせ</a>
  </nav>
</header>

<section class="hero">
  <div class="hero-bg" role="img" aria-label="青空の下に建つ大型工場・倉庫の写真"></div>
  <div class="img" style="left:10px;top:20px;width:210px;height:330px;background:linear-gradient(180deg,#dfe6ee,#9fb0c2);border-radius:10px" role="img" aria-label="ヘルメットをかぶった作業員のイラスト"></div>
  <div class="hero-copy">
    <div class="hero-catch">おまかせください！</div><br>
    <div class="hero-sub">地元新潟の工場倉庫施工に特化したプロ集団による</div><br>
    <div class="hero-main">修繕・改修／増築・新築</div><br>
    <div class="hero-line">外構工事／解体工事／省エネ・コスト削減</div>
  </div>
</section>

<!-- feature -->
<div class="img" style="left:0;top:790px;width:250px;height:380px;background:linear-gradient(135deg,#c8d4de,#7f95a8);border-radius:0 8px 8px 0" role="img" aria-label="工場内部の写真"></div>
<div class="img" style="left:950px;top:760px;width:250px;height:330px;background:linear-gradient(135deg,#dfe6ec,#8ea1b2);border-radius:8px 0 0 8px" role="img" aria-label="倉庫内部の写真"></div>
<div class="sec-head" style="left:300px;top:780px;width:600px;align-items:center">
  <span class="en">FEATURE</span>
  <h2><span class="icon-box"><svg width="24" height="24" viewBox="0 0 24 24"><path fill="#fff" d="M9 3h6v3h5a1 1 0 0 1 1 1v12a1 1 0 0 1-1 1H4a1 1 0 0 1-1-1V7a1 1 0 0 1 1-1h5zm2 2v1h2V5zm0 5v3H8v2h3v3h2v-3h3v-2h-3v-3z"/></svg></span>工場専門修繕サービス</h2>
</div>
<div class="feature-text">
  <p>テキストが入りますテキストが入りますテキストが入りますテキストが入りますテキストが入りますテキストが入りますテキストが入りますテキストが入りますテキストが入ります</p>
  <p>テキストが入りますテキストが入りますテキストが入りますテキストが入りますテキストが入りますテキストが入りますテキストが入りますテキストが入ります</p>
  <p>テキストが入りますテキストが入りますテキストが入りますテキストが入りますテキストが入りますテキストが入りますテキストが入りますテキストが入ります</p>
</div>
<a class="pill" href="#" style="left:470px;top:1280px;width:260px">詳しく見る ›</a>

<!-- works -->
<div class="works-band"></div>
<div class="sec-head light" style="left:150px;top:1460px">
  <span class="en">WORKS</span>
  <h2><svg width="44" height="44" viewBox="0 0 24 24"><path fill="#fff" d="M2 21V9l6 3V9l6 3V5h3l1 2v14z"/></svg>施工実績</h2>
</div>
<a class="pill white" href="#" style="left:870px;top:1490px;width:210px">施工実績一覧 ›</a>
<div class="work-card" style="left:148px"><div class="ph" style="background:linear-gradient(135deg,#6b4b3a,#2f2622)" role="img" aria-label="施工後の工場内部の写真"></div><div class="meta">株式会社○○○○<strong>工場修繕工事</strong></div><span class="arrow-dot"><svg width="12" height="12" viewBox="0 0 12 12"><path d="M4 2l4 4-4 4" stroke="#fff" stroke-width="2" fill="none"/></svg></span></div>
<div class="work-card" style="left:450px"><div class="ph" style="background:linear-gradient(135deg,#7fb4e3,#2a4f7a)" role="img" aria-label="屋根に設置した太陽光パネルの写真"></div><div class="meta">株式会社○○○○<strong>工場増築工事</strong></div><span class="arrow-dot"><svg width="12" height="12" viewBox="0 0 12 12"><path d="M4 2l4 4-4 4" stroke="#fff" stroke-width="2" fill="none"/></svg></span></div>
<div class="work-card" style="left:752px"><div class="ph" style="background:linear-gradient(135deg,#a6cbe8,#7d8a93)" role="img" aria-label="新築した倉庫外観の写真"></div><div class="meta">株式会社○○○○<strong>工場修繕工事</strong></div><span class="arrow-dot"><svg width="12" height="12" viewBox="0 0 12 12"><path d="M4 2l4 4-4 4" stroke="#fff" stroke-width="2" fill="none"/></svg></span></div>

<!-- column -->
<div class="sec-head" style="left:150px;top:2030px">
  <span class="en">COLUMN</span>
  <h2><svg width="44" height="44" viewBox="0 0 24 24"><path fill="#1e78d2" d="M3 17.3V21h3.7L17.8 9.9l-3.7-3.7zM20.7 7a1 1 0 0 0 0-1.4l-2.3-2.3a1 1 0 0 0-1.4 0l-1.8 1.8 3.7 3.7z"/></svg>コラム</h2>
</div>
<a class="pill" href="#" style="left:870px;top:2060px;width:210px">コラム一覧 ›</a>
<div class="col-card" style="left:140px;top:2200px;width:440px;height:460px">
  <div style="height:240px;background:linear-gradient(135deg,#cfe2f2,#8aa4bb)" role="img" aria-label="足場の前で作業する作業員の写真"></div>
  <div style="padding:18px 24px">
    <p class="col-date">2023.11.01</p>
    <p class="col-title">タイトルが入りますタイトルが入りますタイトルが入りますタイトルが入ります</p>
    <p class="col-ex" style="margin-top:12px">記事本文の冒頭が一部表示されます記事本文の冒頭が一部表示されます記事本文の冒頭が一部表示されます…</p>
  </div>
</div>
<div class="col-card" style="left:640px;top:2200px;width:440px;height:220px;display:flex">
  <div style="width:200px;background:linear-gradient(135deg,#d8e2ea,#93a6b6)" role="img" aria-label="倉庫の保管棚の写真"></div>
  <div style="padding:24px 20px;flex:1"><p class="col-date">2023.11.01</p><p class="col-title">タイトルが入りますタイトルが入りますタイトルが入ります</p></div>
</div>
<div class="col-card" style="left:640px;top:2450px;width:440px;height:220px;display:flex">
  <div style="width:200px;background:linear-gradient(135deg,#e8eef3,#a9b8c4)" role="img" aria-label="ヘルメット姿の作業員二人の写真"></div>
  <div style="padding:24px 20px;flex:1"><p class="col-date">2023.11.01</p><p class="col-title">タイトルが入りますタイトルが入りますタイトルが入ります</p></div>
</div>

<!-- news -->
<div class="sec-head" style="left:240px;top:2840px">
  <span class="en">NEWS</span>
  <h2><svg width="44" height="44" viewBox="0 0 24 24"><path fill="#1e78d2" d="M3 10v4h3l5 4V6L6 10zm13 2a4 4 0 0 0-2-3.5v7A4 4 0 0 0 16 12z"/></svg>お知らせ</h2>
</div>
<div class="news-list">
  <div class="news-item"><time>2023.11.01</time><p>テキストが入ります。テキストが入ります。テキストが入ります。テキストが入ります。</p></div>
  <div class="news-item"><time>2023.11.01</time><p>テキストが入ります。テキストが入ります。テキストが入ります。テキストが入ります。</p></div>
  <div class="news-item"><time>2023.11.01</time><p>テキストが入ります。テキストが入ります。テキストが入ります。テキストが入ります。</p></div>
</div>
<a class="pill" href="#" style="left:240px;top:3080px;width:200px">お知らせ一覧 ›</a>

<!-- contents -->
<div class="contents-band"></div>
<div class="contents-box"></div>
<div class="sec-head" style="left:170px;top:3390px">
  <span class="en">CONTENTS</span>
  <h2>コンテンツ</h2>
</div>
<div class="menu-item" style="top:3560px"><span class="ic"><svg width="20" height="20" viewBox="0 0 24 24"><text x="6" y="18" fill="#fff" font-size="18" font-weight="700">?</text></svg></span>よくあるご質問<span class="chev">›</span></div>
<div class="menu-item" style="top:3650px"><span class="ic"><svg width="20" height="20" viewBox="0 0 24 24"><path fill="#fff" d="M3 5h18v14H3zm2 2v.5l7 4.5 7-4.5V7z"/></svg></span>お打ち合わせの流れ<span class="chev">›</span></div>
<div class="menu-item" style="top:3740px"><span class="ic"><svg width="20" height="20" viewBox="0 0 24 24"><path fill="#fff" d="M11 3h2v10l3-3 1.4 1.4L12 16.8l-5.4-5.4L8 10l3 3zM4 19h16v2H4z"/></svg></span>カタログダウンロード<span class="chev">›</span></div>
<div class="img" style="left:580px;top:3470px;width:500px;height:380px;background:linear-gradient(135deg,#f3f6f9,#c6d2dc)" role="img" aria-label="書類を確認する手元の写真"></div>

<!-- contact -->
<div class="img" style="left:70px;top:3980px;width:200px;height:400px;background:linear-gradient(180deg,#dfe6ee,#9fb0c2);border-radius:10px" role="img" aria-label="ヘルメットをかぶった作業員のイラスト"></div>
<div class="sec-head" style="left:300px;top:4010px">
  <span class="en">CONTACT</span>
  <h2>お問い合わせ</h2>
</div>
<p class="contact-lead">ご相談やご質問など、<br>お気軽にお問い合わせください。</p>
<div class="tel-box">
  <small>株式会社○○内 工場修繕部門</small>
  <div class="num"><svg width="24" height="24" viewBox="0 0 24 24"><path fill="#17529c" d="M6.6 10.8a15 15 0 0 0 6.6 6.6l2.2-2.2c.3-.3.7-.4 1-.2 1.1.4 2.3.6 3.6.6.6 0 1 .4 1 1V20c0 .6-.4 1-1 1A17 17 0 0 1 3 4c0-.6.4-1 1-1h3.5c.6 0 1 .4 1 1 0 1.3.2 2.5.6 3.6.1.3 0 .7-.2 1z"/></svg>0120-48-7315</div>
  <small>「工場修繕センターを見た」とお伝えください</small>
</div>
<a class="pill" href="#" style="left:680px;top:4140px;width:400px;height:80px;border-radius:40px;font-size:20px">
  <svg width="26" height="26" viewBox="0 0 24 24"><path fill="#fff" d="M3 5h18v14H3zm2 2v.5l7 4.5 7-4.5V7z"/></svg>無料お見積り・お問い合わせ</a>

<footer class="site-footer">
  <div class="foot-logo">工場修繕センター</div>
  <div class="foot-tel"><svg width="20" height="20" viewBox="0 0 24 24"><path fill="#fff" d="M6.6 10.8a15 15 0 0 0 6.6 6.6l2.2-2.2c.3-.3.7-.4 1-.2 1.1.4 2.3.6 3.6.6.6 0 1 .4 1 1V20c0 .6-.4 1-1 1A17 17 0 0 1 3 4c0-.6.4-1 1-1h3.5c.6 0 1 .4 1 1 0 1.3.2 2.5.6 3.6.1.3 0 .7-.2 1z"/></svg>0120-48-7315</div>
  <div class="foot-col" style="left:440px">ホーム<br>工場修繕センターの特徴<br>施工実績<br>よくあるご質問<br>お打ち合わせの流れ</div>
  <div class="foot-col" style="left:640px">サービス一覧<br>– 修繕・改修<br>– 増築<br>– 新築<br>– 外構工事<br>– 解体工事</div>
  <div class="foot-col" style="left:860px">会社概要<br>コラム<br>お知らせ<br>無料お見積り・お問い合わせ<br>カタログダウンロード</div>
  <div class="foot-copy"><span>プライバシーポリシー　サイトマップ</span><span>Copyright © 工場修繕センター All rights reserved.</span></div>
</footer>

</body>
</html>
```